Maple Vital App Landing Page

Looking for a landing page for our app at maplevitalco.com

Target Market(s)

Health care facilities

Industry/Entity Type

Healthcare

Number of Pages Required

1 page

```html
<!DOCTYPE html>
<html lang="en">
<head>
<meta charset="utf-8">
<title>Maple Vital — App Landing Page</title>
<link href="https://fonts.googleapis.com/css2?family=Montserrat:wght@700&family=Nunito+Sans:wght@300;800&family=Source+Sans+3:wght@400&display=swap" rel="stylesheet">
<style>
  :root {
    --ink: #0a0a0a;
    --body-text: #2e2e2e;
    --sky: #c4effd;
    --white: #ffffff;
    --login-start: #5ef1a8;
    --login-end: #22d676;
    --signup-start: #4fcaf8;
    --signup-end: #1d98d4;
    --art-light: #a9dcf7;
    --art-mid: #6cbdf0;
    --art-deep: #3b6fe0;
  }
  html, body {
    margin: 0;
    padding: 0;
    width: 1200px;
    height: 812px;
    overflow: hidden;
    background: var(--white);
  }
  .page {
    position: relative;
    width: 1200px;
    height: 812px;
    overflow: hidden;
  }
  .backdrop {
    position: absolute;
    inset: 0;
  }
  .brand {
    position: absolute;
    left: 104px;
    top: 50px;
    font-family: "Montserrat", sans-serif;
    font-weight: 700;
    font-size: 24px;
    color: var(--ink);
  }
  .main-nav {
    position: absolute;
    top: 58px;
    left: 553px;
    display: flex;
    align-items: center;
    font-family: "Source Sans 3", sans-serif;
    font-size: 21px;
    letter-spacing: 1.2px;
    color: var(--ink);
  }
  .main-nav a {
    color: inherit;
    text-decoration: none;
    margin-right: 34px;
  }
  .main-nav a.nav-last { margin-right: 31px; }
  .btn {
    display: inline-flex;
    align-items: center;
    justify-content: center;
    border-radius: 21px;
    font-family: "Nunito Sans", sans-serif;
    font-weight: 800;
    color: var(--white);
    text-decoration: none;
    letter-spacing: 0.3px;
  }
  .btn-login {
    width: 112px;
    height: 42px;
    font-size: 15px;
    background: linear-gradient(90deg, var(--login-start), var(--login-end));
  }
  .hero-title {
    position: absolute;
    left: 94px;
    top: 212px;
    margin: 0;
    font-family: "Montserrat", sans-serif;
    font-weight: 700;
    font-size: 88px;
    line-height: 83px;
    color: var(--ink);
    letter-spacing: -0.5px;
  }
  .hero-text {
    position: absolute;
    left: 99px;
    top: 420px;
    width: 380px;
    margin: 0;
    font-family: "Nunito Sans", sans-serif;
    font-weight: 300;
    font-size: 17px;
    line-height: 25.6px;
    color: var(--body-text);
  }
  .btn-signup {
    position: absolute;
    left: 100px;
    top: 557px;
    width: 130px;
    height: 42px;
    font-size: 15px;
    background: linear-gradient(90deg, var(--signup-start), var(--signup-end));
  }
  .hero-art {
    position: absolute;
    left: 612px;
    top: 231px;
    width: 526px;
    height: 381px;
    border-radius: 18px;
    background: linear-gradient(135deg, var(--art-light) 0%, var(--art-mid) 55%, var(--art-deep) 100%);
    opacity: 0.85;
  }
</style>
</head>
<body>
<div class="page">
  <svg class="backdrop" width="1200" height="812" viewBox="0 0 1200 812" aria-hidden="true">
    <path d="M494 0 C480 60 476 130 484 230 C500 420 570 640 657 812 L1200 812 L1200 0 Z" fill="var(--sky)"/>
  </svg>

  <div class="brand">Maple Vital</div>

  <nav class="main-nav">
    <a href="#">Home</a>
    <a href="#">App</a>
    <a href="#">Features</a>
    <a href="#">About</a>
    <a href="#" class="nav-last">Contact</a>
    <a href="#" class="btn btn-login">LOG IN</a>
  </nav>

  <h1 class="hero-title">Loreum<br>Ipsum</h1>

  <p class="hero-text">Lorem ipsum dolor sit amet, consectetur adipiscing elit, sed do eiusmod tempor incididunt ut labore et dolore magna aliqua. Ut enim ad minim veniam, quis nostrud exercitation ullamco laboris nisi ut</p>

  <a href="#" class="btn btn-signup">SIGN UP</a>

  <div class="hero-art" role="img" aria-label="Illustration of a doctor appearing on a large monitor, linked to medical icons and a phone calendar, with a patient pointing at the screen"></div>
</div>
</body>
</html>
```